Banner Ad and Digital Ad design for tradeshow

I need two graphics designed (can be same/similar design just different dimensions. We are an engineering firm practicing in the solid waste industry. We are a conference sponsor and need two graphics.
(1) Banner Ad - 300x250 - gif, png, jped, html, or other. Imagery with our mantra - Driven by purpose. Guided by stewardship. Striving for excellence.
(2) Digital Ad (static) - 1920x1080 hi-res jpg or png.

Target Market(s)

Solid Waste Management Industry (Environmental)

Industry/Entity Type

Environmental

Requirements
Must have
• Quality Aesthetic
Nice to have
• Great Imagery + our mantra

```html
<!DOCTYPE html>
<html lang="en">
<head>
<meta charset="UTF-8">
<title>Verant Engineering – Conference Sponsor Ads</title>
<link rel="stylesheet" href="https://fonts.googleapis.com/css2?family=Montserrat:wght@300;400;600&family=Roboto:wght@400&display=swap">
<style>
  :root {
    --paper: #ffffff;
    --ink-white: #ffffff;
    --kicker: #a9b9ae;
    --dot: #7f8f84;
    --band-dark: #0d0f0e;
    --band-mid: #3e4a43;
    --band-green: #7a9484;
    --band-edge: #8a7a52;
    --sky-top: #3b2b33;
    --sky-pink: #b8606a;
    --sky-orange: #e58a3c;
    --sky-glow: #f2b153;
    --ground: #2a211e;
    --shade: #0e0c0c;
    --label: #111111;
  }
  * { box-sizing: border-box; margin: 0; padding: 0; }
  html, body {
    width: 1200px; height: 535px; overflow: hidden;
    background: var(--paper);
  }
  .board { position: relative; width: 1200px; height: 535px; }

  .ad { position: absolute; overflow: hidden; font-family: "Montserrat", sans-serif; }
  .ad--wide { left: 45px; top: 48px; width: 769px; height: 433px; }
  .ad--square { left: 831px; top: 49px; width: 332px; height: 276px; }

  .ad__photo { position: absolute; inset: 0; }
  .ad--wide .ad__photo {
    background:
      linear-gradient(90deg, rgba(14,12,12,.85) 0%, rgba(14,12,12,.55) 30%, rgba(14,12,12,0) 55%),
      linear-gradient(180deg, transparent 55%, var(--ground) 72%),
      radial-gradient(ellipse 45% 30% at 62% 52%, var(--sky-glow), transparent 70%),
      linear-gradient(180deg, var(--sky-top) 0%, var(--sky-pink) 18%, var(--sky-orange) 40%, #8a5a34 55%, var(--ground) 70%);
  }
  .ad--square .ad__photo {
    background:
      linear-gradient(90deg, rgba(14,12,12,.8) 0%, rgba(14,12,12,.4) 50%, rgba(14,12,12,.1) 100%),
      linear-gradient(180deg, transparent 55%, #2d2622 80%),
      radial-gradient(ellipse 30% 25% at 78% 48%, #f0b35a, transparent 75%),
      linear-gradient(180deg, #1d1b1d 0%, #4a3a33 25%, #b07a3f 45%, #5b4635 60%, #2d2622 80%);
  }

  .ad__band { position: absolute; left: 0; bottom: 0; width: 100%; }
  .ad--wide .ad__band { height: 133px; }
  .ad--square .ad__band { height: 77px; }
  .ad__band svg { display: block; width: 100%; height: 100%; }

  .mantra { position: absolute; color: var(--ink-white); }
  .mantra__kicker {
    position: absolute; left: 0; white-space: nowrap;
    font-weight: 300; color: var(--kicker); text-transform: uppercase;
  }
  .mantra__word {
    position: absolute; left: 0; white-space: nowrap;
    font-weight: 600; text-transform: uppercase; line-height: 1;
  }
  .mantra__dot { color: var(--dot); }

  .ad--wide .mantra { left: 61px; top: 0; }
  .ad--wide .mantra__kicker { font-size: 17px; letter-spacing: 2.2px; line-height: 1; }
  .ad--wide .mantra__word { font-size: 46px; letter-spacing: 2px; }

  .ad--square .mantra { left: 42px; top: 0; }
  .ad--square .mantra__kicker { font-size: 9px; letter-spacing: 1.2px; line-height: 1; }
  .ad--square .mantra__word { font-size: 27px; letter-spacing: 1.2px; }

  .brand {
    position: absolute; display: flex; align-items: center;
    color: var(--ink-white); font-family: "Montserrat", sans-serif; font-weight: 400;
  }
  .brand__mark { background: var(--ink-white); flex: none; }
  .brand__name { display: flex; flex-direction: column; line-height: 1; text-transform: uppercase; }

  .ad--wide .brand { left: 279px; top: 334px; gap: 14px; }
  .ad--wide .brand__mark { width: 49px; height: 49px; }
  .ad--wide .brand__title { font-size: 30px; letter-spacing: 1px; }
  .ad--wide .brand__sub { font-size: 13px; letter-spacing: 7.4px; margin-top: 5px; }

  .ad--square .brand { left: 43px; top: 219px; gap: 7px; }
  .ad--square .brand__mark { width: 28px; height: 28px; }
  .ad--square .brand__title { font-size: 17px; letter-spacing: .6px; }
  .ad--square .brand__sub { font-size: 7.4px; letter-spacing: 4.1px; margin-top: 3px; }

  .size-label {
    position: absolute; font-family: "Roboto", sans-serif;
    font-size: 14px; color: var(--label); line-height: 1;
  }
  .size-label--wide { left: 737px; top: 496px; }
  .size-label--square { left: 1104px; top: 336px; }
</style>
</head>
<body>
<main class="board">

  <section class="ad ad--wide" aria-label="Digital ad 1920 by 1080">
    <div class="ad__photo" role="img" aria-label="Track loader working a landfill at sunset under an orange and pink sky"></div>
    <div class="ad__band">
      <svg viewBox="0 0 769 133" preserveAspectRatio="none" aria-hidden="true">
        <defs>
          <linearGradient id="bandWide" x1="0" x2="1" y1="0" y2="0">
            <stop offset="0" stop-color="var(--band-dark)"/>
            <stop offset=".35" stop-color="var(--band-mid)"/>
            <stop offset=".7" stop-color="var(--band-green)"/>
            <stop offset="1" stop-color="var(--band-green)"/>
          </linearGradient>
        </defs>
        <path d="M0 35 Q384 -35 769 35 L769 133 L0 133 Z" fill="url(#bandWide)"/>
        <path d="M0 35 Q384 -35 769 35" fill="none" stroke="var(--band-edge)" stroke-width="1.5"/>
      </svg>
    </div>
    <div class="mantra">
      <span class="mantra__kicker" style="top:66px">Driven by</span>
      <span class="mantra__word" style="top:86px">Purpose<span class="mantra__dot">.</span></span>
      <span class="mantra__kicker" style="top:142px">Guided by</span>
      <span class="mantra__word" style="top:161px">Stewardship<span class="mantra__dot">.</span></span>
      <span class="mantra__kicker" style="top:215px">Striving for</span>
      <span class="mantra__word" style="top:233px">Excellence<span class="mantra__dot">.</span></span>
    </div>
    <div class="brand">
      <span class="brand__mark"></span>
      <span class="brand__name">
        <span class="brand__title">Verant</span>
        <span class="brand__sub">Engineering</span>
      </span>
    </div>
  </section>

  <section class="ad ad--square" aria-label="Banner ad 300 by 250">
    <div class="ad__photo" role="img" aria-label="Track loader on a landfill with the setting sun behind it"></div>
    <div class="ad__band">
      <svg viewBox="0 0 332 77" preserveAspectRatio="none" aria-hidden="true">
        <defs>
          <linearGradient id="bandSquare" x1="0" x2="1" y1="0" y2="0">
            <stop offset="0" stop-color="var(--band-dark)"/>
            <stop offset=".45" stop-color="var(--band-mid)"/>
            <stop offset="1" stop-color="var(--band-green)"/>
          </linearGradient>
        </defs>
        <path d="M0 10 Q166 -6 332 10 L332 77 L0 77 Z" fill="url(#bandSquare)"/>
      </svg>
    </div>
    <div class="mantra">
      <span class="mantra__kicker" style="top:43px">Driven by</span>
      <span class="mantra__word" style="top:54px">Purpose<span class="mantra__dot">.</span></span>
      <span class="mantra__kicker" style="top:87px">Guided by</span>
      <span class="mantra__word" style="top:97px">Stewardship<span class="mantra__dot">.</span></span>
      <span class="mantra__kicker" style="top:129px">Striving for</span>
      <span class="mantra__word" style="top:139px">Excellence<span class="mantra__dot">.</span></span>
    </div>
    <div class="brand">
      <span class="brand__mark"></span>
      <span class="brand__name">
        <span class="brand__title">Verant</span>
        <span class="brand__sub">Engineering</span>
      </span>
    </div>
  </section>

  <p class="size-label size-label--square">300x250</p>
  <p class="size-label size-label--wide">1920x1080</p>

</main>
</body>
</html>
```